Professional & Modern Website Design for Quarry Roost Fittings

Our company, a leader in custom furniture and joinery solutions for mining camps, needs a website overhaul. Our current site is looking dated and underwhelming, and we’re seeking a design that truly reflects our professionalism and expertise.

To Whom Are We Speaking?
Our target audience includes asset managers, procurement professionals, and senior-level management from international mining companies. We need a website that speaks directly to these key decision-makers, showcasing our value and expertise.

What We’re Looking For:
Fresh & Modern Aesthetic: We want our website to captivate visitors with a contemporary and sleek design.
Professional Appeal: The new design should convey our commitment to high-quality craftsmanship and service.
Visual Impact: Showcase our custom furniture and joinery work with stunning visuals that highlight our capabilities.
Brochure Alignment: The design should mirror the style and aesthetics of our attached brochure to ensure brand consistency and visual harmony.
Logo & Branding: We want to keep our current logo and branding. The red color should be retained but used sparingly as an accent color to complement the overall design.
Brand Book Usage: Attached is our Brand Book for our Hotel and Accommodation Company. Please use only the correct colors and text from this Brand Book for our Quarry Roost Fittings Brand to ensure consistency and coherence across our branding.
Structured Layout: We require a total of 8 pages, including:
Landing Page: Featuring a prominent contact button
About
Services: Interior Design, Manufacturing, Delivery & Installation
Products: Furniture Packages, Joinery, Upholstery, Beds & Bedding

Our Goals:
Elevate Our Brand: Create a site that mirrors our reputation and industry leadership.
Enhance User Experience: Ensure a seamless, engaging experience for visitors.
Showcase Our Work: Promote our projects and services with impact.

Must include:
Contact us button
Geographical Reach

Previous company website: www.quarryroostfittings.com.au (we wish to convert some of the content from this website to the new platform). Competitor websites that we like: www.dovetelle.com.au,

For functionality we would like it to be designed on Wix.

```html
<!DOCTYPE html>
<html lang="en">
<head>
<meta charset="utf-8">
<title>Quarry Roost Fittings</title>
<link href="https://fonts.googleapis.com/css2?family=Outfit:wght@300;400;500;600;700&display=swap" rel="stylesheet">
<style>
:root{
  --ink:#1f2a37;
  --muted:#8a8f97;
  --soft:#f3f3f3;
  --page:#fbfbfb;
  --rule:#cfd2d6;
  --orange:#e38a29;
  --yellow:#f4b400;
  --rust:#b6602f;
  --sand:#d8bfa4;
  --teal:#86a6ae;
  --sage:#b7c8c6;
  --white:#ffffff;
}
*{box-sizing:border-box;margin:0;padding:0}
html,body{width:1200px;height:3502px;overflow:hidden}
body{position:relative;background:var(--page);font-family:'Outfit',sans-serif;color:var(--ink)}
.abs{position:absolute}
a{color:inherit;text-decoration:none}

/* hero */
.hero{left:0;top:0;width:1200px;height:589px;border-radius:0 60px 0 0;overflow:hidden}
.hero-photo{left:0;top:0;width:100%;height:100%;
  background:
    linear-gradient(180deg,rgba(0,0,0,0) 78%,#dca83c 86%,#eec23a 100%),
    linear-gradient(100deg,#a9562b 0%,#c06d3a 40%,#b8632f 60%,#e6d2b6 74%,#efe2cc 100%)}
.brand{left:188px;top:20px;color:var(--white)}
.brand b{display:block;font-size:29px;font-weight:700;letter-spacing:1px;line-height:1}
.brand span{display:block;font-size:12px;letter-spacing:.6px;margin-top:3px}
.nav{left:515px;top:38px;display:flex;align-items:center;color:var(--white);font-size:11px;letter-spacing:.4px}
.nav a{padding:0 16px;border-right:1px solid rgba(255,255,255,.6);line-height:14px}
.nav a:first-child{padding-left:0}
.nav .lang{border:none;opacity:.8}
.menu{left:973px;top:38px;width:18px}
.hero h1{left:188px;top:176px;font-size:36px;font-weight:600;color:var(--white)}
.hero p{left:194px;top:226px;width:285px;font-size:10.5px;line-height:20px;color:#f7e9df}
.more{display:flex;align-items:center;gap:12px;font-size:11px;font-weight:500}
.ring{width:22px;height:22px;border-radius:50%;border:2px dashed currentColor}
.hero .more{left:194px;top:299px;color:var(--white)}
.buy{left:1074px;top:268px;width:126px;height:34px;background:var(--white);display:flex;align-items:center;gap:8px;padding-left:14px;font-size:13px;border-radius:4px 0 0 4px}
.buy b{font-weight:700}

/* titles */
.sec-title{left:0;width:1200px;text-align:center;font-size:19px;font-weight:500;letter-spacing:.3px}
.sec-sub{left:0;width:1200px;text-align:center;font-size:10px;color:var(--muted);line-height:17px}
.rule{left:188px;width:824px;height:1px;background:var(--rule)}

/* picks */
.pick{top:719px;width:268px;height:148px;border-radius:10px;overflow:hidden;color:var(--white)}
.pick-photo{position:absolute;left:0;top:0;width:100%;height:100%}
.pick small{position:absolute;left:20px;top:35px;font-size:7px;letter-spacing:.8px;opacity:.8}
.pick b{position:absolute;left:20px;top:48px;font-size:12px;font-weight:500}
.pick svg{position:absolute;left:20px;top:80px}

/* panels */
.panel{background:var(--soft);border-radius:10px}
.photo{border-radius:10px}
.panel h2{position:absolute;font-size:32px;font-weight:400;line-height:38px}
.panel h2 b{font-weight:600}
.panel p{position:absolute;font-size:11px;line-height:17.5px}
.hl{color:var(--yellow)}

.orange-card{background:var(--orange);border-radius:10px;color:var(--white)}

/* partners */
.badge{top:2494px;width:44px;height:60px;display:flex;flex-direction:column;align-items:center;gap:6px}
.badge i{display:block;width:40px;height:40px;border-radius:50%;border:2px solid #333}
.badge u{display:block;width:34px;height:5px;background:#333;border-radius:2px;text-decoration:none}

/* form */
.field{left:194px;width:399px;height:26px;border:1px solid #9aa0a6;border-radius:4px;font-size:10px;display:flex;align-items:center;gap:8px;padding-left:10px;background:var(--white)}
.field.note{align-items:flex-start;padding-top:8px;height:102px}
.send{left:194px;top:2926px;width:397px;height:26px;background:var(--yellow);border-radius:3px;color:var(--white);font-size:10px;display:flex;align-items:center;justify-content:center}
.follow{left:614px;top:2857px;width:397px;height:24px;background:var(--orange);border-radius:3px;color:var(--white);font-size:10px;display:flex;align-items:center;justify-content:space-between;padding:0 20px}
.dots{display:flex;gap:8px}
.dots i{width:7px;height:7px;border-radius:50%;background:var(--white)}

/* perks */
.perk-t{font-size:11px;font-weight:600}
.perk-s{font-size:9px;color:#b5b9bf;line-height:15px;margin-top:5px}

/* footer */
.footer{left:0;top:3153px;width:1200px;height:349px;background:#f5f6f8}
.fcol{top:3207px;font-size:11px;color:#555}
.fcol h4{font-size:11px;font-weight:400;margin-bottom:22px}
.fcol li{list-style:none;color:#8a8f97;font-size:10px;height:26.5px}
.legal{top:3460px;font-size:9px;color:#555}
.legal a{text-decoration:underline;margin-left:14px}
</style>
</head>
<body>

<!-- HERO -->
<section class="abs hero">
  <div class="abs hero-photo" role="img" aria-label="Upholstered lounge chair and shell chair beside a round wooden side table, against a rust and cream backdrop on a yellow floor"></div>
  <div class="abs brand"><b>QUARRY</b><span>ROOST FITTINGS</span></div>
  <nav class="abs nav">
    <a>ABOUT</a><a>SERVICES</a><a>PRODUCTS</a><a>CONTACT US</a><a class="lang">EN ⌄</a>
  </nav>
  <svg class="abs menu" viewBox="0 0 18 12" height="12"><path d="M0 1h18M3 6h15M0 11h18" stroke="#fff" stroke-width="1.4"/></svg>
  <h1 class="abs">WELCOME</h1>
  <p class="abs">From concept development to space planning and material selection, we ensure that our interior design solutions align with your vision and operational goals.</p>
  <a class="abs more"><span class="ring"></span>View More</a>
</section>
<a class="abs buy"><svg width="20" height="16" viewBox="0 0 20 16"><path d="M1 2h3l2 9h10l2-7H5" fill="#f4b400"/><circle cx="8" cy="14" r="1.5" fill="#f4b400"/><circle cx="15" cy="14" r="1.5" fill="#f4b400"/></svg>BUY <b>NOW</b></a>

<!-- COVERED -->
<h2 class="abs sec-title" style="top:629px">WE HAVE YOU COVERED FROM</h2>
<p class="abs sec-sub" style="top:667px">It is a long established fact that a reader will be distracted by the</p>

<a class="abs pick" style="left:185px">
  <span class="pick-photo" role="img" aria-label="Black desk lamp on a teal background" style="background:linear-gradient(120deg,#86a6ae,#7c9aa2)"></span>
  <small>TOP PICKS</small><b>Custom woodwork</b>
  <svg width="14" height="10" viewBox="0 0 14 10"><path d="M0 5h12M8 1l4 4-4 4" stroke="#fff" fill="none"/></svg>
</a>
<a class="abs pick" style="left:467px">
  <span class="pick-photo" role="img" aria-label="Wooden bar stool on a sand background" style="background:linear-gradient(120deg,#d8bfa4,#d2b595)"></span>
  <small>TOP PICKS</small><b>Custom woodwork</b>
  <svg width="14" height="10" viewBox="0 0 14 10"><path d="M0 5h12M8 1l4 4-4 4" stroke="#fff" fill="none"/></svg>
</a>
<a class="abs pick" style="left:750px">
  <span class="pick-photo" role="img" aria-label="Pale ceramic vase on a sage background" style="background:linear-gradient(120deg,#b7c8c6,#afc2c0)"></span>
  <small>TOP PICKS</small><b>Custom woodwork</b>
  <svg width="14" height="10" viewBox="0 0 14 10"><path d="M0 5h12M8 1l4 4-4 4" stroke="#fff" fill="none"/></svg>
</a>

<div class="abs rule" style="top:930px"></div>

<!-- CONCEPT -->
<div class="abs panel" style="left:188px;top:993px;width:405px;height:267px">
  <h2 style="left:45px;top:26px"><span class="hl">Concept</span> to<br>Completion</h2>
  <p style="left:45px;top:109px;width:275px">Whether you require interior design expertise, assistance with tender submissions, custom joinery solutions, or furniture and room prototypes, we have the expertise and resources to deliver exceptional results.</p>
  <a class="abs more" style="left:45px;top:207px"><span class="ring" style="color:var(--yellow)"></span>View More</a>
</div>
<div class="abs photo" role="img" aria-label="Accommodation room interior with desk, orange chair and wardrobe" style="left:607px;top:993px;width:405px;height:244px;background:linear-gradient(110deg,#d9d6d1,#b8a48a 55%,#a67a4f)"></div>

<div class="abs photo" role="img" aria-label="Wall-mounted timber bedside panel with reading light" style="left:0;top:1301px;width:173px;height:243px;border-radius:0 10px 10px 0;background:linear-gradient(120deg,#cbb79f,#a88a6b 60%,#c58b68)"></div>
<div class="abs photo" role="img" aria-label="Bed base with timber storage drawer and white linen" style="left:188px;top:1301px;width:405px;height:243px;background:linear-gradient(150deg,#f1efec 40%,#b98553 60%,#e8e3dc)"></div>
<div class="abs panel" style="left:607px;top:1301px;width:405px;height:243px">
  <h2 style="left:45px;top:28px"><b>Durable,</b> functional<br>and compliant</h2>
  <p style="left:45px;top:108px;width:258px">We understand the unique demands of mining operations and the need for durable, functional, and compliant furniture solutions. With our comprehensive packages, we aim to create comfortable and efficient living spaces for your mining workforce.</p>
</div>

<!-- SERVICES -->
<h2 class="abs sec-title" style="top:1600px">OUR SERVICES</h2>
<p class="abs sec-sub" style="top:1634px">We pay our respect to their Elders past and present and extend that respect to all Aboriginal and<br>Torres Strait Islander peoples.</p>

<div class="abs orange-card" style="left:188px;top:1707px;width:334px;height:283px">
  <h2 class="abs" style="left:27px;top:26px;font-size:32px;font-weight:400;line-height:38px"><b style="font-weight:600">Special</b> order<br>production</h2>
  <p class="abs" style="left:27px;top:116px;width:275px;font-size:11px;line-height:17.5px;color:#fbe6cc">Whether you require interior design expertise, assistance with tender submissions, custom joinery solutions, or furniture and room prototypes, we have the expertise and resources to deliver exceptional results.</p>
  <a class="abs more" style="left:27px;top:214px"><span class="ring"></span>Learn More</a>
</div>
<div class="abs photo" role="img" aria-label="Joiner operating a timber machine in the workshop" style="left:538px;top:1707px;width:473px;height:283px;background:linear-gradient(100deg,#9b8f82,#4a5a7a 45%,#2c3e6b 60%,#8a6a4a)"></div>

<div class="abs rule" style="top:2048px"></div>

<!-- GEO -->
<div class="abs panel" style="left:189px;top:2100px;width:397px;height:253px">
  <h2 style="left:42px;top:40px"><span style="font-weight:400">Geographical</span><br><b>Reach</b></h2>
  <p style="left:42px;top:126px;width:268px">With a global presence, our services extend to Australia, New Zealand, South East Asia, and the United Arab Emirates.</p>
  <a class="abs more" style="left:42px;top:183px"><span class="ring" style="color:var(--yellow)"></span>View More</a>
</div>
<div class="abs" role="img" aria-label="World map highlighting Australia, New Zealand, South East Asia and the UAE" style="left:605px;top:2105px;width:265px;height:240px;border-radius:10px;background:radial-gradient(circle at 62% 55%,#c89a55 0 22%,#e7e8ea 40%,#f4f4f5 75%)"></div>
<div class="abs" style="left:887px;top:2100px;width:124px;height:253px;background:var(--yellow);border-radius:4px"></div>

<!-- PARTNERS -->
<h2 class="abs sec-title" style="top:2402px">BUSINESS PARTNERS</h2>
<p class="abs sec-sub" style="top:2445px">It is a long established fact that a reader will be distracted by the</p>
<div class="abs badge" style="left:257px"><i></i><u></u></div>
<div class="abs badge" style="left:424px"><i></i><u></u></div>
<div class="abs badge" style="left:606px"><i></i><u></u></div>
<div class="abs badge" style="left:758px"><i style="border-radius:4px"></i><u></u></div>
<div class="abs badge" style="left:897px"><i></i><u></u></div>

<div class="abs rule" style="top:2594px"></div>

<!-- CONTACT -->
<form>
  <label class="abs field" style="top:2647px"><svg width="10" height="11" viewBox="0 0 10 11"><circle cx="5" cy="3" r="2.5" fill="none" stroke="#333"/><path d="M0.5 11c0-3 2-4.5 4.5-4.5S9.5 8 9.5 11" fill="none" stroke="#333"/></svg>Name Surname</label>
  <label class="abs field" style="top:2688px"><svg width="10" height="11" viewBox="0 0 10 11"><circle cx="5" cy="3" r="2.5" fill="none" stroke="#333"/><path d="M0.5 11c0-3 2-4.5 4.5-4.5S9.5 8 9.5 11" fill="none" stroke="#333"/></svg>E-Mail</label>
  <label class="abs field" style="top:2728px"><svg width="10" height="11" viewBox="0 0 10 11"><path d="M1 .5h5l3 3v7H1z" fill="none" stroke="#333"/></svg>Choose file</label>
  <label class="abs field" style="top:2768px"><b style="font-size:8px">+90</b>Cep Telefon Numarası</label>
  <label class="abs field note" style="top:2809px"><svg width="10" height="10" viewBox="0 0 10 10"><rect x=".5" y=".5" width="9" height="9" rx="2" fill="none" stroke="#333"/><path d="M3 5h4" stroke="#333"/></svg>Note</label>
  <button class="abs send" type="button" style="border:none;font-family:inherit">Send</button>
</form>

<div class="abs panel" style="left:614px;top:2643px;width:397px;height:200px">
  <h3 class="abs" style="left:29px;top:30px;font-size:22px;font-weight:400;line-height:26px"><b style="font-weight:600">Industry experts.</b> At your<br>service</h3>
  <p style="left:29px;top:88px;width:250px;font-size:10px;line-height:16px">You have questions. We have answers. Fill out this form to start the conversation.</p>
  <p style="left:29px;top:135px;width:240px;font-size:10px;line-height:16px">Are you an existing customer looking for technical help? <a style="color:var(--orange);text-decoration:underline;font-weight:600">Connect here.</a></p>
</div>
<div class="abs follow"><span>Follow Us</span><span class="dots"><i></i><i></i><i></i><i></i></span></div>
<a class="abs panel" style="left:614px;top:2892px;width:397px;height:60px;display:flex;align-items:center;justify-content:space-between;padding:0 40px 0 21px;font-size:10px"><span><b>Download</b> our service <b>catalogue</b></span><svg width="16" height="16" viewBox="0 0 16 16"><path d="M1 15L15 1M5 1h10v10" stroke="#333" fill="none" stroke-width="1.4"/></svg></a>

<div class="abs rule" style="top:3001px"></div>

<!-- PERKS -->
<svg class="abs" style="left:238px;top:3060px" width="40" height="40" viewBox="0 0 40 40"><circle cx="20" cy="20" r="18" fill="none" stroke="#333" stroke-width="1.4"/><path d="M11 14h3l3 10h10l2-7H15" fill="none" stroke="#333" stroke-width="1.4"/><circle cx="18" cy="28" r="1.5" fill="#333"/><circle cx="25" cy="28" r="1.5" fill="#333"/></svg>
<div class="abs" style="left:294px;top:3058px"><div class="perk-t">20 day returns</div><div class="perk-s">Vel risus commodo viverra<br>maecenas accumsan.</div></div>
<svg class="abs" style="left:462px;top:3058px" width="36" height="42" viewBox="0 0 36 42"><path d="M2 4h6l6 26h16" fill="none" stroke="#333" stroke-width="1.4"/><rect x="14" y="10" width="14" height="12" fill="none" stroke="#333" stroke-width="1.4" transform="rotate(-12 21 16)"/><circle cx="14" cy="35" r="3" fill="none" stroke="#333" stroke-width="1.4"/></svg>
<div class="abs" style="left:516px;top:3058px"><div class="perk-t">Free Shipping</div><div class="perk-s">Vel risus commodo viverra<br>maecenas accumsan.</div></div>
<div class="abs" style="left:686px;top:3055px;width:252px">
  <div style="font-size:14px;font-weight:500">Sign up for our newsletter</div>
  <div style="margin-top:18px;border-bottom:1px solid #555;display:flex;justify-content:space-between;font-size:9px;color:#777;padding-bottom:4px"><span>Your Email</span><svg width="12" height="8" viewBox="0 0 12 8"><path d="M0 4h10M7 1l3 3-3 3" stroke="#333" fill="none"/></svg></div>
</div>

<!-- FOOTER -->
<footer class="abs footer"></footer>
<div class="abs" style="left:194px;top:3207px;color:#3a3f45">
  <b style="display:block;font-size:28px;font-weight:700;letter-spacing:1px;line-height:1">QUARRY</b>
  <span style="display:block;font-size:12px;letter-spacing:.5px;margin-top:3px">ROOST FITTINGS</span>
  <p style="width:140px;font-size:7px;line-height:15px;color:#777;margin-top:12px">Fittings and joinery crafted for remote camps. Durable pieces made for crews, delivered and installed with care across each region.</p>
  <div style="display:flex;gap:5px;margin-top:8px"><i style="width:10px;height:10px;border-radius:50%;background:#555"></i><i style="width:10px;height:10px;border-radius:50%;background:#555"></i><i style="width:10px;height:10px;border-radius:50%;background:#555"></i></div>
</div>
<div class="abs fcol" style="left:421px"><h4>Pages</h4><ul><li>page</li><li>page</li><li>page</li><li>page</li><li>page</li><li>page</li><li>page</li></ul></div>
<div class="abs fcol" style="left:580px"><h4>Utility Pages</h4><ul><li>page</li><li>page</li><li>page</li><li>404 Page</li><li>page</li></ul></div>
<div class="abs fcol" style="left:738px"><h4>Pages</h4><ul><li>page</li><li>page</li><li>page</li><li>page</li><li>page</li><li>page</li><li>page</li></ul></div>
<div class="abs fcol" style="left:867px"><h4>Utility Pages</h4><ul><li>page</li><li>page</li><li>page</li><li>page</li><li>page</li></ul></div>
<div class="abs legal" style="left:191px">Copyright © 2023. All Rights Reserved.</div>
<div class="abs legal" style="left:620px"><a>Information Society Services</a><a>Personal Data Protection Law</a><a>Privacy Policy</a></div>

</body>
</html>
```